Dental Office Needs- Flyer Design for Same Day Crowns

We need a flyer that will explain the benefits of the same day crown from the patient prospective. Not show pictures of the machine that makes the crowns. See attached material for content. The flyer should use the practices PMS colors of Green 562 and Blue 3025. The ad should say to the patient - I want to go this office and get my crown done there.
Updates

Project Deadline Extended Reason: The difference in the time zone between USA and Europe has caused issues. Minor changes still need to be worked out. Added Thursday, July 14, 2016

Target Market(s)

Dental Patients

Industry/Entity Type

Dental

Requirements
Must have
• Call to Action
• Business Address and Business Logo
• Classic Design
• images of a Happy 50 year old Couple
• Gives the benefits of the same day crown
Should not have
• No Images of tooth figures
• No before or after pictures

```html
<!DOCTYPE html>
<html lang="en">
<head>
<meta charset="utf-8">
<title>Brookfield Dental Care – One Visit Crowns</title>
<link href="https://fonts.googleapis.com/css2?family=Oswald:wght@400;600&family=Questrial&family=PT+Sans+Narrow:wght@400;700&family=PT+Sans:wght@400;700&display=swap" rel="stylesheet">
<style>
  :root {
    --green: #00806e;
    --navy: #005482;
    --sky: #a6d8f5;
    --ink: #1d4a78;
    --white: #ffffff;
    --photo-light: #f3e6dc;
    --photo-mid: #d9a785;
  }
  * { margin: 0; padding: 0; box-sizing: border-box; }
  html, body { width: 927px; height: 1200px; overflow: hidden; background: var(--white); }
  .flyer { position: relative; width: 927px; height: 1200px; overflow: hidden; background: var(--white); }
  .backdrop { position: absolute; inset: 0; width: 927px; height: 1200px; }

  .farewells { position: absolute; top: 14px; left: 0; width: 927px; height: 100px; }
  .farewell { position: absolute; top: 0; text-align: center; color: var(--green); transform: translateX(-50%); white-space: nowrap; }
  .farewell-word { font-family: "Oswald", sans-serif; font-weight: 600; font-size: 48px; line-height: 58px; letter-spacing: 0.5px; }
  .farewell-item { font-family: "Oswald", sans-serif; font-weight: 400; font-size: 28px; line-height: 34px; transform: scaleX(0.85); }

  .intro { position: absolute; left: 30px; top: 186px; width: 360px; font-family: "Questrial", sans-serif; font-size: 23.5px; line-height: 28.5px; color: var(--ink); letter-spacing: 0.4px; }

  .offer { position: absolute; left: 60px; top: 780px; width: 330px; font-family: "PT Sans Narrow", sans-serif; font-size: 24px; line-height: 50px; color: var(--white); }
  .offer strong { font-weight: 700; }

  .explainer { position: absolute; left: 456px; top: 752px; width: 420px; font-family: "PT Sans Narrow", sans-serif; font-size: 21.5px; line-height: 43px; color: var(--ink); }

  .brand-card { position: absolute; left: 38px; top: 956px; width: 360px; height: 196px; background: var(--white); border-radius: 14px; box-shadow: inset 0 6px 8px rgba(0,0,0,0.18); display: flex; align-items: center; justify-content: center; gap: 10px; }
  .brand-dot { width: 14px; height: 14px; border-radius: 50%; background: var(--green); flex: none; }
  .brand-name { font-family: "PT Sans Narrow", sans-serif; font-weight: 400; font-size: 34px; color: var(--navy); }

  .contact { position: absolute; left: 520px; top: 990px; width: 374px; height: 220px; background: var(--navy); border-radius: 14px 14px 0 0; color: var(--white); text-align: center; font-family: "PT Sans", sans-serif; padding-top: 12px; }
  .contact-cta { font-size: 28px; line-height: 38px; }
  .contact-phone { font-weight: 700; font-size: 34px; line-height: 46px; letter-spacing: 0.5px; }
  .contact-address { font-size: 28px; line-height: 43px; }
</style>
</head>
<body>
<main class="flyer">
  <svg class="backdrop" viewBox="0 0 1159 1500" aria-hidden="false">
    <defs>
      <radialGradient id="couple-tone" cx="0.55" cy="0.4" r="0.6">
        <stop offset="0" stop-color="var(--photo-mid)"/>
        <stop offset="1" stop-color="var(--photo-light)"/>
      </radialGradient>
    </defs>
    <rect class="couple-photo" x="380" y="180" width="779" height="700" fill="url(#couple-tone)" role="img" aria-label="Photo of a smiling, happy couple in their fifties embracing"/>
    <path class="band-green-left" d="M0,425 C30,510 80,590 125,635 L0,720 Z" fill="var(--green)"/>
    <path class="field-sky" d="M0,470 C90,760 390,905 630,905 C880,905 1080,790 1159,650 L1159,1500 L0,1500 Z" fill="var(--sky)"/>
    <path class="band-green-right" d="M1159,1020 C1090,1200 880,1410 460,1500 L1159,1500 Z" fill="var(--green)"/>
    <path class="band-green-bottom" d="M0,1250 C150,1360 300,1430 460,1500 L0,1500 Z" fill="var(--green)"/>
    <path class="field-navy" d="M10,515 C70,640 130,690 175,685 C300,800 450,870 620,870 C860,870 1070,760 1159,625 L1159,655 C1070,800 880,905 630,905 L520,905 L520,1435 Q520,1460 495,1460 L35,1460 Q10,1460 10,1435 Z" fill="var(--navy)"/>
  </svg>

  <header class="farewells">
    <div class="farewell" style="left:182px"><div class="farewell-word">GOOD-BYE</div><div class="farewell-item">TEMPORARY CROWN</div></div>
    <div class="farewell" style="left:446px"><div class="farewell-word">GOOD-BYE</div><div class="farewell-item">SECOND APPOINTMENT</div></div>
    <div class="farewell" style="left:726px"><div class="farewell-word">GOOD-BYE</div><div class="farewell-item">GOOEY MESSY IMPRESSIONS</div></div>
  </header>

  <p class="intro">When it comes to your next crown, the benefits of a Digital Restoration add up quickly!</p>

  <p class="offer"><strong>Brookfield Dental Care</strong> is pleased to offer you the Comfort and Convenience&nbsp; of One Visit Dental Care.</p>

  <p class="explainer">Restorative dentistry has evolved and now, digital technology allows us to take an impression of your teeth with a digital scanner and create your restoration right in our office.</p>

  <div class="brand-card">
    <span class="brand-dot"></span>
    <span class="brand-name">Brookfield Dental Care</span>
  </div>

  <section class="contact">
    <p class="contact-cta">Call Us Today</p>
    <p class="contact-phone">555-014-2273</p>
    <p class="contact-address">418 E. Maple Road,<br>Lakeview, MI</p>
  </section>
</main>
</body>
</html>
```